SunMeadow Yoga Website Design

Business Logo - attached
5 pages being:
Home
About
Classes
Blog
Contact

Would like Scrolling webpage and yoga symbols to be used.

Must have's being:
Easy to navigate, Text needs to be able to be edited/updated, Enquire Now Links, More Information Links, be a secure site, SEO,

Please refer to attached document for the information for the body of the website.

Target Market(s)

Educators, Community Service, Health and Wellbeing, Mental Health

Industry/Entity Type

Yoga

Coding

Coded - Design and coding required

Number of Pages Required

5+ page

Font styles to use
Other font styles liked:
• Bella Bold BC

Colors
0094D4
00A9DD
6FCCEA
C7EBF8
E9F6FB
6B429C
8869AF
B7A5CE
E3DAEB
F3F0F8

Requirements
Must have
• Easy to navigate, Text needs to be able to be edited/updated, Enquire Now Links, More Information Links, be a secure site, SEO,
Nice to have
• Scrolling webpage, yoga symbols

```html
<!DOCTYPE html>
<html lang="en">
<head>
<meta charset="utf-8">
<title>SunMeadow Yoga – Home Page Layouts</title>
<link href="https://fonts.googleapis.com/css2?family=Arimo:wght@400;700&family=Kaushan+Script&family=Playfair+Display:wght@400;700&display=swap" rel="stylesheet">
<style>
:root{
  --backdrop:#d4b8f8;
  --ink:#111111;
  --violet:#5b1fb0;
  --violet-deep:#4a2a8e;
  --plum:#8a3fa0;
  --royal:#5b2db0;
  --ocean:#1e6fb8;
  --teal:#1fa3b4;
  --aqua:#22b0cf;
  --aqua-light:#1fc6d8;
  --lilac:#d9cdf0;
  --mist:#f5f5f6;
  --footer:#4b4390;
  --body-text:#333333;
  --muted:#666666;
  --white:#ffffff;
}
*{margin:0;padding:0;box-sizing:border-box}
html,body{width:734px;height:1200px;overflow:hidden;background:var(--backdrop)}
.stage{position:relative;width:1506px;height:2464px;transform:scale(0.48738);transform-origin:0 0;background:var(--backdrop);font-family:"Arimo",Arial,sans-serif;color:var(--body-text)}
.sample-title{position:absolute;top:88px;width:300px;text-align:center;font-family:"Playfair Display",Georgia,serif;font-weight:700;font-size:32px;color:var(--ink)}
.page{position:absolute;top:152px;width:566px;height:2191px;background:var(--white);overflow:hidden}
.page > *{position:absolute}
.topbar{left:0;top:0;width:566px;height:25px;background:linear-gradient(90deg,#3a2f8f 0%,#1e9db0 50%,#6b429c 100%);display:flex;align-items:center;justify-content:flex-end;gap:8px;padding-right:60px;color:var(--white);font-family:"Playfair Display",Georgia,serif;font-size:9px}
.topbar .item{display:flex;align-items:center;gap:4px}
.topbar .dot{width:8px;height:8px;border-radius:50%;background:var(--white)}
.brand-badge{left:54px;top:3px;width:64px;height:64px;border-radius:50%;background:var(--white);display:flex;align-items:center;justify-content:center;text-align:center;font-family:"Playfair Display",Georgia,serif;font-size:9px;line-height:1.1;color:var(--violet);z-index:2}
.nav{left:190px;top:46px;display:flex;gap:0;font-family:"Playfair Display",Georgia,serif;font-size:9px;color:#333}
.nav a{display:block;width:48px;text-align:left;text-decoration:none;color:inherit}
.nav a.active{color:var(--violet-deep)}
.nav-underline{left:203px;top:64px;width:22px;height:2px;background:var(--violet-deep)}
.pill{display:flex;align-items:center;justify-content:center;border-radius:14px;background:linear-gradient(90deg,#6b2fc8,#1fa3b4);color:var(--white);font-family:"Playfair Display",Georgia,serif;font-weight:700}
.nav-btn{left:446px;top:38px;width:61px;height:24px;font-size:8px}
.hero{left:0;top:75px;width:566px;height:273px;background:linear-gradient(180deg,#5a2d8c 0%,#3f64a8 45%,#1fc6d8 100%)}
.hero-ring{position:absolute;border:2px solid rgba(199,175,240,0.7);border-radius:50%}
.hero-name{position:absolute;font-family:"Kaushan Script",cursive;color:var(--white);white-space:nowrap}
.hero-btn{position:absolute;border:2px solid var(--white);font-size:11px}
.script-title{left:0;width:566px;text-align:center;font-family:"Kaushan Script",cursive;font-size:30px;color:var(--violet)}
.photo{position:absolute}
.frame{position:absolute;border:2px solid var(--lilac)}
.copy{font-size:8.4px;line-height:10.4px;color:var(--body-text)}
.copy p+p{margin-top:10px}
.more-btn{left:268px;top:595px;width:111px;height:23px;font-size:10px}
.benefits{left:0;top:674px;width:566px;height:184px;background:var(--aqua);text-align:center;color:var(--white)}
.benefits h2{font-family:"Kaushan Script",cursive;font-weight:400;font-size:30px;margin-top:36px}
.benefits p{font-size:8.4px;line-height:10px;width:330px;margin:10px auto 0}
.benefits h3{font-family:"Kaushan Script",cursive;font-weight:400;font-size:19px;margin-top:14px}
.mist{left:0;top:858px;width:566px;height:863px;background:var(--mist)}
.topic-title{font-family:"Kaushan Script",cursive;font-weight:400;font-size:22px}
.topic-list{list-style:none;font-size:8.4px;line-height:10px;color:var(--body-text)}
.topic-list li{position:relative;padding-left:9px;margin-bottom:6px}
.topic-list li::before{content:"";position:absolute;left:0;top:2px;width:4px;height:4px;border:1.5px solid var(--royal);border-radius:50%}
.accent{position:absolute}
.closing{left:83px;top:1590px;width:400px;text-align:center;font-size:10px;line-height:11.8px;color:var(--muted)}
.closing p+p{margin-top:12px}
.field-label{font-size:8.4px;color:#444}
.field-line{height:1px;background:#d8d8d8}
.submit-btn{left:244px;top:1914px;width:79px;height:24px;font-size:9px}
.footer{left:0;top:1998px;width:566px;height:193px;background:var(--footer);color:var(--white)}
.footer > *{position:absolute}
.footer h4{font-family:"Kaushan Script",cursive;font-weight:400;font-size:16px}
.footer-lines{font-size:8px;line-height:14.5px}
.footer-lines div{display:flex;align-items:center;gap:4px}
.footer-brand{left:248px;top:24px;width:72px;height:72px;border-radius:50%;border:1.5px solid rgba(255,255,255,0.5);display:flex;align-items:center;justify-content:center;text-align:center;font-family:"Playfair Display",Georgia,serif;font-size:10px;line-height:1.2;color:var(--white)}
.footer-rule{left:60px;top:134px;width:446px;height:1px;background:rgba(255,255,255,0.35)}
.copyright{left:0;top:150px;width:566px;text-align:center;font-size:8.4px}
.social-dot{width:8px;height:8px;border-radius:50%;background:var(--white);display:inline-block}
</style>
</head>
<body>
<div class="stage">
  <div class="sample-title" style="left:251px">Sample 1</div>
  <div class="sample-title" style="left:947px">Sample 2</div>

  <!-- Layout one -->
  <section class="page" style="left:126px">
    <div class="topbar">
      <span class="item"><svg width="9" height="7" viewBox="0 0 9 7"><rect x="0.5" y="0.5" width="8" height="6" fill="none" stroke="#fff"/><path d="M0.5 0.5l4 3 4-3" fill="none" stroke="#fff"/></svg>info@sunmeadowyoga.com.au</span>
      <span class="item"><svg width="8" height="8" viewBox="0 0 10 10"><path d="M2 0.5l2 2.5-1 1.3c.6 1.3 1.5 2.2 2.8 2.8l1.3-1 2.4 2-1.2 1.6C4.5 9.5.5 5.5.5 1.7z" fill="#fff"/></svg>Call Us: 0400 555 128</span>
      <span class="dot"></span><span class="dot"></span>
    </div>
    <div class="brand-badge">SunMeadow<br>Yoga</div>
    <nav class="nav"><a class="active">Home</a><a>About</a><a>Classes</a><a>Blog</a><a>Contact</a></nav>
    <div class="nav-underline"></div>
    <div class="pill nav-btn">Enquire Now</div>

    <header class="hero">
      <div class="hero-ring" style="left:62px;top:25px;width:222px;height:222px"></div>
      <div class="hero-name" style="left:309px;width:230px;top:94px;font-size:26px;text-align:center">SunMeadow Yoga</div>
      <div class="pill hero-btn" style="left:381px;top:142px;width:86px;height:25px">Enquire Now</div>
    </header>

    <h1 class="script-title" style="top:375px">Welcome to SunMeadow Yoga...</h1>
    <div class="frame" style="left:43px;top:549px;width:97px;height:88px"></div>
    <div class="photo" role="img" aria-label="Photo of a person meditating cross-legged on a yoga mat" style="left:60px;top:440px;width:198px;height:180px;background:linear-gradient(135deg,#e9e4dc,#b9b0a6 60%,#8e99a8)"></div>
    <div class="copy" style="left:268px;top:440px;width:228px">
      <p>SunMeadow Yoga believe that you are never too young to benefit from and fall in love with yoga. My aim is to EMPOWER kids and teens to thrive by teaching life skills in Yoga, Mindfulness and Breathing techniques to deal with daily challenges and big emotions.</p>
      <p>SunMeadow Yoga gives kids an opportunity to enjoy and experience yoga for themselves and primarily focuses on programs for Schools, Pre Schools and Early Learning Centres, Private Classes, Sporting Clubs, Martial Arts Schools, Scout Groups and Occupational Therapy Centres just to name a few. All classes are age appropriate and encourage children's natural drive to learn, move, and be creative.</p>
    </div>
    <div class="pill more-btn">More Information</div>

    <section class="benefits">
      <h2>Benefits of Yoga...</h2>
      <p>The benefits of yoga can last a lifetime. It is my aim &amp; passion to introduce yoga to kids of all ages and backgrounds so that they can not only experience the benefits of yoga but fall in love with the practice.</p>
      <h3>Yoga benefits include:</h3>
    </section>

    <div class="mist"></div>
    <h3 class="topic-title" style="left:60px;top:902px;color:var(--plum)">Healthy Bodies</h3>
    <ul class="topic-list" style="left:60px;top:942px;width:200px">
      <li>Develops strong, flexible and healthy bodies</li><li>Promotes spinal alignment and good posture</li><li>Builds energy and stamina</li><li>Improves internal physical function - organs, digestion, elimination, circulation, and blood flow.</li><li>Helps breathing and lung capacity</li><li>Teaches the enjoyment of movement</li><li>Works the 'whole' body</li>
    </ul>
    <svg class="accent" style="left:432px;top:1004px" width="91" height="85"><defs><linearGradient id="a1" x1="0" x2="1"><stop offset="0" stop-color="#a54fb0"/><stop offset="1" stop-color="#6b3fa8"/></linearGradient></defs><path d="M83 0h8v85H0v-8h83z" fill="url(#a1)"/></svg>
    <div class="photo" role="img" aria-label="Photo of children doing bridge poses in a bright room" style="left:277px;top:916px;width:232px;height:157px;background:linear-gradient(160deg,#f2efe9,#c9c1b4 55%,#6f7d8c)"></div>

    <svg class="accent" style="left:30px;top:1213px" width="91" height="84"><defs><linearGradient id="a2" x1="0" x2="1"><stop offset="0" stop-color="#6b2fc8"/><stop offset="1" stop-color="#1fa3b4"/></linearGradient></defs><path d="M0 0h8v76h83v8H0z" fill="url(#a2)"/></svg>
    <div class="photo" role="img" aria-label="Photo of smiling children sitting on colourful mats with hands raised" style="left:44px;top:1128px;width:232px;height:156px;background:linear-gradient(160deg,#f4efe8,#e9a7b8 55%,#5aa0d8)"></div>
    <h3 class="topic-title" style="left:310px;top:1136px;color:var(--royal)">Healthy Minds</h3>
    <ul class="topic-list" style="left:310px;top:1176px;width:230px">
      <li>Cultivates confidence and self-esteem</li><li>Develops concentration and attention</li><li>Clears the mind for better clarity and decision making</li><li>Helps relax and sleep better</li><li>Calms the nervous system</li><li>Learns to cope with stressful situations</li><li>Balances emotions</li>
    </ul>

    <h3 class="topic-title" style="left:60px;top:1346px;color:var(--ocean)">Healthy Spirits</h3>
    <ul class="topic-list" style="left:60px;top:1386px;width:200px">
      <li>Fosters creativity, expression and imagination</li><li>Cultivates kindness to themselves and others</li><li>Cultivates respect for self and others</li><li>Builds balance and inner quiet</li><li>Builds inner strength and resilience</li><li>Teaches self-awareness</li><li>Focuses on positive self-talk</li>
    </ul>
    <svg class="accent" style="left:423px;top:1447px" width="91" height="84"><defs><linearGradient id="a3" x1="0" x2="1"><stop offset="0" stop-color="#6b2fc8"/><stop offset="1" stop-color="#1fa3b4"/></linearGradient></defs><path d="M83 0h8v84H0v-8h83z" fill="url(#a3)"/></svg>
    <div class="photo" role="img" aria-label="Photo of a yoga class stretching in a row on mats" style="left:268px;top:1359px;width:233px;height:156px;background:linear-gradient(160deg,#f1eeea,#b8ada3 55%,#4d4a4f)"></div>

    <div class="closing">
      <p>SunMeadow Yoga combines all the benefits of traditional yoga and a lot of fun! We play games and practice engaging flows which get our bodies moving, then we take a quiet moment to be still and calm as we focus on our breathing.</p>
      <p>SunMeadow Yoga Kids will learn that relaxation is just as important as moving their bodies, and the exercises which they learn in class can easily be repeated at any time in their busy day to feel calm and grounded.</p>
    </div>

    <h2 class="script-title" style="top:1740px">Contact Us</h2>
    <div class="field-label" style="left:94px;top:1795px">Name:</div><div class="field-line" style="left:94px;top:1815px;width:182px"></div>
    <div class="field-label" style="left:291px;top:1795px">Phone:</div><div class="field-line" style="left:291px;top:1815px;width:183px"></div>
    <div class="field-label" style="left:94px;top:1829px">Email:</div><div class="field-line" style="left:94px;top:1848px;width:182px"></div>
    <div class="field-label" style="left:291px;top:1829px">Subject:</div><div class="field-line" style="left:291px;top:1848px;width:183px"></div>
    <div class="field-label" style="left:94px;top:1863px">Message:</div><div class="field-line" style="left:94px;top:1901px;width:372px"></div>
    <div class="pill submit-btn">Submit Now</div>

    <footer class="footer">
      <h4 style="left:60px;top:26px">Contact Us</h4>
      <div class="footer-lines" style="left:60px;top:52px">
        <div><svg width="8" height="8" viewBox="0 0 8 8"><circle cx="4" cy="2.3" r="2" fill="#fff"/><path d="M0 8a4 3 0 0 1 8 0z" fill="#fff"/></svg>Contact: Hannah Wellsby</div>
        <div><svg width="8" height="8" viewBox="0 0 10 10"><path d="M2 0.5l2 2.5-1 1.3c.6 1.3 1.5 2.2 2.8 2.8l1.3-1 2.4 2-1.2 1.6C4.5 9.5.5 5.5.5 1.7z" fill="#fff"/></svg>Phone: 0400 555 128</div>
        <div><svg width="8" height="6" viewBox="0 0 9 7"><rect width="9" height="7" fill="#fff"/><path d="M0 0l4.5 3.5L9 0" fill="none" stroke="#4b4390"/></svg>Email: info@sunmeadowyoga.com.au</div>
        <div><svg width="7" height="9" viewBox="0 0 10 12"><path d="M5 0a4 4 0 0 1 4 4c0 3-4 8-4 8S1 7 1 4a4 4 0 0 1 4-4z" fill="#fff"/></svg>Location: Fernvale, Victoria Australia 3999</div>
      </div>
      <div class="footer-brand">SunMeadow<br>Yoga</div>
      <h4 style="left:350px;top:26px">Connect With Us</h4>
      <div class="footer-lines" style="left:350px;top:52px">
        <div><span class="social-dot"></span>Social page: SunMeadow Yoga</div>
        <div><span class="social-dot"></span>Photo feed: sunmeadowyoga4kids</div>
        <div style="margin-top:10px;padding-left:4px">ABN: 12 345 678 901</div>
      </div>
      <div class="footer-rule"></div>
      <div class="copyright">Copyright 2023 SunMeadow Yoga</div>
    </footer>
  </section>

  <!-- Layout two -->
  <section class="page" style="left:786px">
    <div class="topbar">
      <span class="item"><svg width="9" height="7" viewBox="0 0 9 7"><rect x="0.5" y="0.5" width="8" height="6" fill="none" stroke="#fff"/><path d="M0.5 0.5l4 3 4-3" fill="none" stroke="#fff"/></svg>info@sunmeadowyoga.com.au</span>
      <span class="item"><svg width="8" height="8" viewBox="0 0 10 10"><path d="M2 0.5l2 2.5-1 1.3c.6 1.3 1.5 2.2 2.8 2.8l1.3-1 2.4 2-1.2 1.6C4.5 9.5.5 5.5.5 1.7z" fill="#fff"/></svg>Call Us: 0400 555 128</span>
      <span class="dot"></span><span class="dot"></span>
    </div>
    <div class="brand-badge">SunMeadow<br>Yoga</div>
    <nav class="nav"><a class="active">Home</a><a>About</a><a>Classes</a><a>Blog</a><a>Contact</a></nav>
    <div class="nav-underline"></div>
    <div class="pill nav-btn" style="font-family:'Kaushan Script',cursive;font-weight:400">Enquire Now</div>

    <header class="hero">
      <div class="hero-ring" style="left:195px;top:55px;width:176px;height:176px"></div>
      <div class="hero-name" style="left:0;width:566px;top:128px;text-align:center;font-family:'Playfair Display',Georgia,serif;font-size:20px">SunMeadow Yoga</div>
    </header>

    <h1 class="script-title" style="top:375px">Welcome to SunMeadow Yoga...</h1>
    <div class="frame" style="left:43px;top:549px;width:97px;height:88px"></div>
    <div class="photo" role="img" aria-label="Photo of a person meditating cross-legged on a yoga mat" style="left:60px;top:440px;width:198px;height:180px;background:linear-gradient(135deg,#e9e4dc,#b9b0a6 60%,#8e99a8)"></div>
    <div class="copy" style="left:268px;top:440px;width:228px">
      <p>SunMeadow Yoga believe that you are never too young to benefit from and fall in love with yoga. My aim is to EMPOWER kids and teens to thrive by teaching life skills in Yoga, Mindfulness and Breathing techniques to deal with daily challenges and big emotions.</p>
      <p>SunMeadow Yoga gives kids an opportunity to enjoy and experience yoga for themselves and primarily focuses on programs for Schools, Pre Schools and Early Learning Centres, Private Classes, Sporting Clubs, Martial Arts Schools, Scout Groups and Occupational Therapy Centres just to name a few. All classes are age appropriate and encourage children's natural drive to learn, move, and be creative.</p>
    </div>
    <div class="pill more-btn">More Information</div>

    <section class="benefits">
      <h2>Benefits of Yoga...</h2>
      <p>The benefits of yoga can last a lifetime. It is my aim &amp; passion to introduce yoga to kids of all ages and backgrounds so that they can not only experience the benefits of yoga but fall in love with the practice.</p>
      <h3>Yoga benefits include:</h3>
    </section>

    <div class="mist"></div>
    <h3 class="topic-title" style="left:60px;top:902px;color:var(--plum)">Healthy Bodies</h3>
    <ul class="topic-list" style="left:60px;top:942px;width:200px">
      <li>Develops strong, flexible and healthy bodies</li><li>Promotes spinal alignment and good posture</li><li>Builds energy and stamina</li><li>Improves internal physical function - organs, digestion, elimination, circulation, and blood flow.</li><li>Helps breathing and lung capacity</li><li>Teaches the enjoyment of movement</li><li>Works the 'whole' body</li>
    </ul>
    <svg class="accent" style="left:432px;top:1004px" width="91" height="85"><defs><linearGradient id="b1" x1="0" x2="1"><stop offset="0" stop-color="#a54fb0"/><stop offset="1" stop-color="#6b3fa8"/></linearGradient></defs><path d="M83 0h8v85H0v-8h83z" fill="url(#b1)"/></svg>
    <div class="photo" role="img" aria-label="Photo of young women holding plank poses on pink mats" style="left:277px;top:916px;width:232px;height:157px;background:linear-gradient(160deg,#f3efea,#d9c3bb 55%,#e59ab4)"></div>

    <svg class="accent" style="left:30px;top:1213px" width="91" height="84"><defs><linearGradient id="b2" x1="0" x2="1"><stop offset="0" stop-color="#6b2fc8"/><stop offset="1" stop-color="#1fa3b4"/></linearGradient></defs><path d="M0 0h8v76h83v8H0z" fill="url(#b2)"/></svg>
    <div class="photo" role="img" aria-label="Photo of a girl meditating on a purple mat in a living room" style="left:44px;top:1128px;width:232px;height:156px;background:linear-gradient(160deg,#e8e6df,#9fa98f 50%,#8a62b8)"></div>
    <h3 class="topic-title" style="left:310px;top:1136px;color:var(--royal)">Healthy Minds</h3>
    <ul class="topic-list" style="left:310px;top:1176px;width:230px">
      <li>Cultivates confidence and self-esteem</li><li>Develops concentration and attention</li><li>Clears the mind for better clarity and decision making</li><li>Helps relax and sleep better</li><li>Calms the nervous system</li><li>Learns to cope with stressful situations</li><li>Balances emotions</li>
    </ul>

    <h3 class="topic-title" style="left:60px;top:1346px;color:var(--ocean)">Healthy Spirits</h3>
    <ul class="topic-list" style="left:60px;top:1386px;width:200px">
      <li>Fosters creativity, expression and imagination</li><li>Cultivates kindness to themselves and others</li><li>Cultivates respect for self and others</li><li>Builds balance and inner quiet</li><li>Builds inner strength and resilience</li><li>Teaches self-awareness</li><li>Focuses on positive self-talk</li>
    </ul>
    <svg class="accent" style="left:423px;top:1447px" width="91" height="84"><defs><linearGradient id="b3" x1="0" x2="1"><stop offset="0" stop-color="#6b2fc8"/><stop offset="1" stop-color="#1fa3b4"/></linearGradient></defs><path d="M83 0h8v84H0v-8h83z" fill="url(#b3)"/></svg>
    <div class="photo" role="img" aria-label="Photo of three young women doing side stretches on orange mats" style="left:268px;top:1359px;width:233px;height:156px;background:linear-gradient(160deg,#eef0f2,#b7c2cc 50%,#f0a070)"></div>

    <div class="closing">
      <p>SunMeadow Yoga combines all the benefits of traditional yoga and a lot of fun! We play games and practice engaging flows which get our bodies moving, then we take a quiet moment to be still and calm as we focus on our breathing.</p>
      <p>SunMeadow Yoga Kids will learn that relaxation is just as important as moving their bodies, and the exercises which they learn in class can easily be repeated at any time in their busy day to feel calm and grounded.</p>
    </div>

    <h2 class="script-title" style="top:1740px">Contact Us</h2>
    <div class="field-label" style="left:94px;top:1795px">Name:</div><div class="field-line" style="left:94px;top:1815px;width:182px"></div>
    <div class="field-label" style="left:291px;top:1795px">Phone:</div><div class="field-line" style="left:291px;top:1815px;width:183px"></div>
    <div class="field-label" style="left:94px;top:1829px">Email:</div><div class="field-line" style="left:94px;top:1848px;width:182px"></div>
    <div class="field-label" style="left:291px;top:1829px">Subject:</div><div class="field-line" style="left:291px;top:1848px;width:183px"></div>
    <div class="field-label" style="left:94px;top:1863px">Message:</div><div class="field-line" style="left:94px;top:1901px;width:372px"></div>
    <div class="pill submit-btn">Submit Now</div>

    <footer class="footer">
      <h4 style="left:60px;top:26px">Contact Us</h4>
      <div class="footer-lines" style="left:60px;top:52px">
        <div><svg width="8" height="8" viewBox="0 0 8 8"><circle cx="4" cy="2.3" r="2" fill="#fff"/><path d="M0 8a4 3 0 0 1 8 0z" fill="#fff"/></svg>Contact: Hannah Wellsby</div>
        <div><svg width="8" height="8" viewBox="0 0 10 10"><path d="M2 0.5l2 2.5-1 1.3c.6 1.3 1.5 2.2 2.8 2.8l1.3-1 2.4 2-1.2 1.6C4.5 9.5.5 5.5.5 1.7z" fill="#fff"/></svg>Phone: 0400 555 128</div>
        <div><svg width="8" height="6" viewBox="0 0 9 7"><rect width="9" height="7" fill="#fff"/><path d="M0 0l4.5 3.5L9 0" fill="none" stroke="#4b4390"/></svg>Email: info@sunmeadowyoga.com.au</div>
        <div><svg width="7" height="9" viewBox="0 0 10 12"><path d="M5 0a4 4 0 0 1 4 4c0 3-4 8-4 8S1 7 1 4a4 4 0 0 1 4-4z" fill="#fff"/></svg>Location: Fernvale, Victoria Australia 3999</div>
      </div>
      <div class="footer-brand">SunMeadow<br>Yoga</div>
      <h4 style="left:350px;top:26px">Connect With Us</h4>
      <div class="footer-lines" style="left:350px;top:52px">
        <div><span class="social-dot"></span>Social page: SunMeadow Yoga</div>
        <div><span class="social-dot"></span>Photo feed: sunmeadowyoga4kids</div>
        <div style="margin-top:10px;padding-left:4px">ABN: 12 345 678 901</div>
      </div>
      <div class="footer-rule"></div>
      <div class="copyright">Copyright 2023 SunMeadow Yoga</div>
    </footer>
  </section>
</div>
</body>
</html>
```